HVAC company business card design

We need a business card design for a HVAC company. The design must look professional. Both sides will be used. The total data to be on the business card is
Name
Position
Email
Direct Phone/Moile Phone
Company Contacts /Address, Phone, Fax, web)
All data will be submit once the design is confirmed. For generic purposes use;
Emre Toksoy
Managing Director
+902324815263 (Mobile)
4712 Sokak No: 9 KBSE Yenikent IZMIR TURKEY
Tel: +902324815263 Fax : +902324815269
www.luvon.com.tr

Target Market(s)

HVAC

Industry/Entity Type

Business

Contact Information for Business Card

The total data to be on the business card is
Name
Position
Email
Direct Phone/Moile Phone
Emre Toksoy
Managing Director
+902324815263 (Mobile)
www.luvon.com.tr
The BC will use both sides of the card. The front will include the full logo and the details for the business card holder. The business card can be divided into vertical/horizontal or to a special shape. The common data like the company address/phone/fax should be indicated elsewehere. The back can contain some part or the whole logo and must contain the web address.

Font styles to use
Serif
Sans Serif

Colors
0355a3
cfdfed

Requirements
Should not have
• Please be careful with the fonts, it shouldnt be too small or too big and must not interfere with the logo fonts. If you need to use a curvy shape please do not use as the logo is already curvy or use the curves from the logo (if it looks good, otherwise forget it)
• We are not in favor of pictograms, only if they are perfect use them.

```html
<!DOCTYPE html>
<html lang="en">
<head>
<meta charset="utf-8">
<title>LUVON Business Card – Front and Back</title>
<link rel="stylesheet" href="https://fonts.googleapis.com/css2?family=Play:wght@400;700&display=swap">
<style>
  :root {
    --brand-blue: #3565b8;
    --brand-navy: #2c3552;
    --soft-blue: #cfdfed;
    --paper: #ffffff;
    --stage: #e9ebef;
    --rule: #3565b8;
  }
  * { box-sizing: border-box; margin: 0; padding: 0; }
  html, body { width: 1200px; height: 800px; overflow: hidden; }
  body {
    background: var(--stage);
    font-family: "Play", "Segoe UI", sans-serif;
    color: var(--brand-navy);
    position: relative;
  }
  .card {
    position: absolute;
    width: 540px;
    height: 309px;
    background: var(--paper);
    box-shadow: 0 8px 24px rgba(30, 40, 70, 0.18);
    overflow: hidden;
  }
  .card--back { left: 30px; top: 245px; }
  .card--front { left: 630px; top: 245px; }

  .wordmark {
    position: absolute;
    display: flex;
    align-items: center;
    gap: 12px;
  }
  .wordmark__dot {
    width: 40px; height: 40px;
    border-radius: 50%;
    background: var(--brand-blue);
  }
  .wordmark__name {
    font-weight: 700;
    font-size: 46px;
    letter-spacing: 2px;
    color: var(--brand-navy);
    line-height: 1;
  }

  /* Front */
  .card--front .wordmark { left: 38px; top: 92px; }
  .divider {
    position: absolute;
    left: 312px; top: 58px;
    width: 2px; height: 142px;
    background: var(--rule);
  }
  .holder { position: absolute; left: 330px; top: 62px; }
  .holder__name { font-size: 28px; color: var(--brand-navy); line-height: 1.1; }
  .holder__title { font-size: 14px; color: var(--brand-blue); margin-bottom: 12px; }
  .contact-list { list-style: none; }
  .contact-list li {
    display: flex; align-items: center; gap: 7px;
    font-size: 13.5px; line-height: 22px; color: var(--brand-navy);
  }
  .contact-list svg { width: 15px; height: 15px; flex: none; }
  .address-band {
    position: absolute;
    left: 0; right: 0; top: 222px;
    height: 26px;
    background: var(--brand-blue);
    color: var(--paper);
    font-size: 13px;
    line-height: 26px;
    padding-left: 60px;
    letter-spacing: 0.3px;
  }

  /* Back */
  .card--back .wordmark { left: 70px; top: 108px; }
  .back-web {
    position: absolute; left: 58px; top: 214px;
    font-size: 15px; font-weight: 700; color: var(--brand-blue);
  }
  .back-decoration {
    position: absolute;
    right: -30px; top: 40px;
    width: 300px; height: 300px;
    background: radial-gradient(closest-side, rgba(207, 223, 237, 0.85), rgba(207, 223, 237, 0.35) 70%, rgba(207, 223, 237, 0));
  }
</style>
</head>
<body>

<section class="card card--back" aria-label="Card back">
  <div class="back-decoration" role="img" aria-label="Faint enlarged brand symbol in soft blue tones"></div>
  <div class="wordmark">
    <span class="wordmark__dot"></span>
    <span class="wordmark__name">LUVON</span>
  </div>
  <p class="back-web">www.luvon.com.tr</p>
</section>

<section class="card card--front" aria-label="Card front">
  <div class="wordmark">
    <span class="wordmark__dot"></span>
    <span class="wordmark__name">LUVON</span>
  </div>
  <div class="divider"></div>
  <div class="holder">
    <p class="holder__name">Emre Toksoy</p>
    <p class="holder__title">Managing Director</p>
    <ul class="contact-list">
      <li>
        <svg viewBox="0 0 16 16" aria-hidden="true"><circle cx="8" cy="8" r="8" fill="var(--brand-blue)"/><rect x="5" y="3.5" width="6" height="9" rx="1" fill="none" stroke="#fff" stroke-width="1.3"/></svg>
        +902324815263
      </li>
      <li>
        <svg viewBox="0 0 16 16" aria-hidden="true"><circle cx="8" cy="8" r="8" fill="var(--brand-blue)"/><path d="M5 4.5c.6-.4 1.2-.3 1.5.3l.6 1.3c.2.4 0 .8-.3 1l-.5.4c.4.9 1.1 1.7 2 2.1l.4-.5c.3-.3.7-.4 1-.2l1.3.6c.6.3.6.9.3 1.5-.5.9-1.5 1.2-2.6.6C6.6 10.5 5.4 9.2 4.6 7.3c-.4-1.1-.3-2.2.4-2.8z" fill="#fff"/></svg>
        +902324815263
      </li>
      <li>
        <svg viewBox="0 0 16 16" aria-hidden="true"><circle cx="8" cy="8" r="8" fill="var(--brand-blue)"/><rect x="4" y="6.5" width="8" height="5" rx="0.8" fill="#fff"/><rect x="5.5" y="3.8" width="5" height="3" fill="none" stroke="#fff" stroke-width="1.1"/></svg>
        +902324815269
      </li>
      <li>
        <svg viewBox="0 0 16 16" aria-hidden="true"><circle cx="8" cy="8" r="8" fill="var(--brand-blue)"/><circle cx="8" cy="8" r="4.2" fill="none" stroke="#fff" stroke-width="1.1"/><ellipse cx="8" cy="8" rx="1.8" ry="4.2" fill="none" stroke="#fff" stroke-width="1"/><line x1="3.8" y1="8" x2="12.2" y2="8" stroke="#fff" stroke-width="1"/></svg>
        www.luvon.com.tr
      </li>
    </ul>
  </div>
  <p class="address-band">4712 Sokak No: 9 KBSE Yenikent IZMIR TURKEY</p>
</section>

</body>
</html>
```